VFX Company Business Card Design Project

The Ember Vale is a decentralized Visual Effects Studio servicing the television and feature film industries.
Project Brief:
Take our logo that was previously designed on Pixel Harbor and make a double sided business card.
Requirements:
- Card MUST be double sided.
- Front of card MUST have the yellow part of our logo against the dark grey background.
- Back of card is completely up to the designer.
- Back of card must include the complete company logo.
Please follow these File Preparation guidelines:
http://printmoor.example/infopage?file=filetype_en&s=PrintMoor_new&lang=en
Industry/Entity Type
Business
Look and feel
Each slider illustrates characteristics of the customer's brand and the style your logo design should communicate.

```html
<!DOCTYPE html>
<html lang="en">
<head>
<meta charset="utf-8">
<title>The Ember Vale — Business Card</title>
<link rel="stylesheet" href="https://fonts.googleapis.com/css2?family=Questrial&family=Jura:wght@400;500&display=swap">
<style>
  :root {
    --sky-top: #22f4f6;
    --sky-bottom: #ffffff;
    --card-grey: #47555a;
    --brand-yellow: #fccc14;
    --bar-yellow: #f2e600;
    --bar-shade: #c9c000;
    --name-ink: #2a2f31;
    --contact-ink: #dfe6e8;
    --pattern-tone: rgba(120, 138, 100, 0.16);
    --edge-ink: #2c3436;
  }
  * { margin: 0; padding: 0; box-sizing: border-box; }
  html, body { width: 1200px; height: 1050px; overflow: hidden; }
  body {
    position: relative;
    background: linear-gradient(to bottom, var(--sky-top) 0%, #a9f8f8 55%, var(--sky-bottom) 100%);
    font-family: "Questrial", sans-serif;
  }
  .card {
    position: absolute;
    width: 670px;
    height: 453px;
    border-radius: 4px;
    overflow: hidden;
    background:
      repeating-conic-gradient(from 0deg at 85% 30%, rgba(255,255,255,0.018) 0deg 2deg, transparent 2deg 7deg),
      var(--card-grey);
  }
  .card--front { left: 36px; top: 41px; }
  .card--back { left: 474px; top: 542px; width: 668px; }

  .stripe-bar { position: absolute; top: 29px; height: 43px; background: linear-gradient(to bottom, var(--bar-shade), var(--bar-yellow)); }

  .wordmark {
    position: absolute;
    color: var(--brand-yellow);
    font-family: "Questrial", sans-serif;
    font-weight: 400;
    white-space: nowrap;
  }
  .card--front .wordmark { left: 30px; top: 96px; font-size: 38px; }

  .name-band {
    position: absolute;
    left: 294px; top: 147px;
    width: 376px; height: 50px;
    background: linear-gradient(to right, rgba(255,255,255,0) 0%, #e8eeee 22%, #aab4b5 55%, #5f6c70 100%);
    clip-path: polygon(2% 8%, 100% 0, 100% 100%, 0 92%);
  }
  .holder-name {
    position: absolute;
    right: 36px; top: 146px;
    font-family: "Jura", sans-serif;
    font-size: 42px;
    letter-spacing: 1px;
    color: var(--name-ink);
    white-space: nowrap;
  }
  .holder-role {
    position: absolute;
    right: 40px; top: 197px;
    font-family: "Jura", sans-serif;
    font-size: 20px;
    color: var(--name-ink);
  }
  .contact {
    position: absolute;
    left: 377px; top: 318px;
    list-style: none;
    font-size: 22px;
    line-height: 30px;
    color: var(--contact-ink);
    white-space: nowrap;
  }

  .pattern-field {
    position: absolute;
    background: var(--pattern-tone);
    -webkit-mask-image: radial-gradient(ellipse at center, #000 35%, transparent 75%);
    mask-image: radial-gradient(ellipse at center, #000 35%, transparent 75%);
  }
  .pattern-field--top { left: 120px; top: -20px; width: 580px; height: 190px; }
  .pattern-field--bottom { left: -40px; top: 270px; width: 740px; height: 210px; }
  .swoosh { position: absolute; inset: 0; }
  .card--back .wordmark { left: 52px; top: 168px; font-size: 80px; }
</style>
</head>
<body>

  <section class="card card--front" aria-label="Card front">
    <div class="stripe-bar" style="left:0;width:292px"></div>
    <div class="stripe-bar" style="left:298px;width:132px"></div>
    <div class="stripe-bar" style="left:435px;width:87px"></div>
    <div class="stripe-bar" style="left:527px;width:57px"></div>
    <div class="stripe-bar" style="left:589px;width:35px"></div>
    <div class="stripe-bar" style="left:629px;width:12px"></div>
    <div class="stripe-bar" style="left:646px;width:8px"></div>
    <div class="stripe-bar" style="left:659px;width:11px"></div>

    <div class="wordmark">The Ember Vale</div>

    <div class="name-band"></div>
    <div class="holder-name">Your Name</div>
    <div class="holder-role">Position</div>

    <ul class="contact">
      <li>Address here</li>
      <li>hello@embervale.example</li>
      <li>www.embervale.example</li>
    </ul>
  </section>

  <section class="card card--back" aria-label="Card back">
    <div class="pattern-field pattern-field--top" role="img" aria-label="Faint repeating brand pattern"></div>
    <div class="pattern-field pattern-field--bottom" role="img" aria-label="Faint repeating brand pattern"></div>
    <svg class="swoosh" viewBox="0 0 668 453" width="668" height="453" aria-hidden="true">
      <path d="M0,0 H284 C240,40 205,70 150,72 C92,74 42,110 0,152 Z" fill="var(--brand-yellow)" stroke="var(--edge-ink)" stroke-width="1"/>
      <path d="M668,297 C642,340 622,360 590,362 C520,364 440,392 374,453 H668 Z" fill="var(--brand-yellow)" stroke="var(--edge-ink)" stroke-width="1"/>
    </svg>
    <div class="wordmark">The Ember Vale</div>
  </section>

</body>
</html>
```